Business Cards Needed For Veterinary Business

Looking for a business card design for a veterinary blood bank. We would like it to be clean and professional on appearance but still warm and inviting. We would like to utilize our logo and similar coloring. We will use our phone number, email, website, employee name, employee title.

We do not want a bunch of animated animal photos but do not need the style to be as clinical as a laboratory or human medical procedure office.

We are looking for some creative ideas to choose from so that we can generate a standout professional business card for our management team to utilize.

Target Market(s)

professionals

Industry/Entity Type

veterinary

Contact Information for Business Card

employee name, employee title, phone number, website URL, email

Font styles to use
Sans Serif

Colors
0054AA
0677BA
7BADD7
CADEEF
E8F1F8
EB3D1F
EC4F4E
F09395
F8D3D4
FCEDEE

Requirements
Nice to have
• creative design
Should not have
• animated photos

```html
<!DOCTYPE html>
<html lang="en">
<head>
<meta charset="utf-8">
<title>Larkspur Pet Blood Bank – Business Card</title>
<link rel="stylesheet" href="https://fonts.googleapis.com/css2?family=Montserrat:wght@600;700&family=Poppins:wght@400&display=swap">
<style>
  :root {
    --stage: #8a8a8a;
    --brand-blue: #0e4f92;
    --brand-red: #ec1c24;
    --paper: #ffffff;
    --ink-gray: #6d6e71;
  }
  html, body {
    margin: 0;
    padding: 0;
    width: 1093px;
    height: 1200px;
    overflow: hidden;
    background: var(--stage);
  }
  .canvas {
    position: relative;
    width: 1093px;
    height: 1200px;
  }
  .card {
    position: absolute;
    left: 264px;
    width: 580px;
    height: 356px;
    border-radius: 26px;
    overflow: hidden;
  }
  .card--front { top: 226px; background: var(--brand-blue); }
  .card--back  { top: 621px; background: var(--paper); }

  .front-red-panel {
    position: absolute;
    top: 0; right: 0;
    width: 154px;
    height: 100%;
    background: var(--brand-red);
  }
  .front-mark-area {
    position: absolute;
    left: 324px;
    top: 140px;
    width: 204px;
    height: 204px;
    border-radius: 50%;
    background: var(--paper);
  }
  .name-marker {
    position: absolute;
    left: 0; top: 82px;
    width: 12px; height: 41px;
    background: var(--brand-red);
  }
  .holder {
    position: absolute;
    left: 26px; top: 77px;
    color: var(--paper);
  }
  .holder-name {
    margin: 0;
    font: 700 25px/1 "Montserrat", sans-serif;
    color: var(--brand-red);
    letter-spacing: -0.3px;
  }
  .holder-title {
    margin: 1px 0 0;
    font: 400 17px/1.1 "Poppins", sans-serif;
  }
  .contact {
    position: absolute;
    left: 26px; top: 204px;
    margin: 0; padding: 0;
    list-style: none;
    color: var(--paper);
    font: 400 18px/21px "Poppins", sans-serif;
  }
  .contact li { display: flex; align-items: center; gap: 7px; }
  .contact svg { width: 15px; height: 15px; flex: none; }

  .back-brand {
    position: absolute;
    left: 0; right: 0;
    top: 0; bottom: 0;
    display: flex;
    align-items: center;
    justify-content: center;
    gap: 12px;
  }
  .brand-dot {
    width: 40px; height: 40px;
    border-radius: 50%;
    background: var(--brand-red);
  }
  .brand-name {
    margin: 0;
    font: 700 26px/1 "Montserrat", sans-serif;
    color: var(--brand-red);
    letter-spacing: -0.3px;
  }
  .back-band {
    position: absolute;
    bottom: 0;
    height: 11px;
  }
  .back-band--red  { left: 0; width: 293px; background: var(--brand-red); }
  .back-band--blue { right: 0; width: 284px; background: var(--brand-blue); }
</style>
</head>
<body>
<main class="canvas">
  <section class="card card--front" aria-label="Card front">
    <div class="front-red-panel"></div>
    <div class="front-mark-area" role="img" aria-label="Brand mark area"></div>
    <div class="name-marker"></div>
    <div class="holder">
      <h1 class="holder-name">DANIEL REYES</h1>
      <p class="holder-title">Managing Director</p>
    </div>
    <ul class="contact">
      <li>
        <svg viewBox="0 0 16 16" aria-hidden="true"><path fill="#ec1c24" d="M3.5 1.5l2.5 2.7-1.4 1.7c.9 2 2.6 3.7 4.6 4.6l1.7-1.4 2.7 2.5-1.4 2.3C7.2 13.6 2.4 8.8 1.2 3z"/></svg>
        055-987 210 346
      </li>
      <li>
        <svg viewBox="0 0 16 16" aria-hidden="true"><rect x="1" y="3.5" width="14" height="9" fill="#ec1c24"/><path d="M1 3.5l7 5 7-5" fill="none" stroke="#0e4f92" stroke-width="1.2"/></svg>
        hello@larkspurpbb.com
      </li>
      <li>
        <svg viewBox="0 0 16 16" aria-hidden="true"><g fill="none" stroke="#ec1c24" stroke-width="1.3"><circle cx="8" cy="8" r="6.5"/><ellipse cx="8" cy="8" rx="2.8" ry="6.5"/><path d="M1.5 8h13M2.5 4.8h11M2.5 11.2h11"/></g></svg>
        www.larkspurpbb.com
      </li>
    </ul>
  </section>

  <section class="card card--back" aria-label="Card back">
    <div class="back-brand">
      <span class="brand-dot"></span>
      <p class="brand-name">Larkspur Pet Blood Bank</p>
    </div>
    <div class="back-band back-band--red"></div>
    <div class="back-band back-band--blue"></div>
  </section>
</main>
</body>
</html>
```